biz card for insurance Agent
Insurance Agency Biz card
biz card for insurance Agent - Health
Creative Brief
Professional
Marla Tovesby
Insurance Agent
NC & SC
marlatovesby@quillmail.example
please create a design for the back of the card, and we'll add the text to it later

```html
<!DOCTYPE html>
<html lang="en">
<head>
<meta charset="utf-8">
<title>Brightline Coverage Co. – Business Cards</title>
<link href="https://fonts.googleapis.com/css2?family=Roboto:wght@400;500;700;900&display=swap" rel="stylesheet">
<style>
  :root {
    --stage: #e4e4e4;
    --card: #ffffff;
    --crimson: #8e1a1e;
    --crimson-dark: #5e0f12;
    --red: #d3232a;
    --ink: #1a1a1a;
    --black: #0d0d0d;
    --rule: #9a9a9a;
    --muted: #555555;
  }
  * { box-sizing: border-box; margin: 0; padding: 0; }
  html, body { width: 1200px; height: 698px; overflow: hidden; }
  body {
    background: var(--stage);
    font-family: "Roboto", Arial, sans-serif;
    position: relative;
  }
  .card {
    position: absolute;
    top: 194px;
    width: 540px;
    height: 310px;
    background: var(--card);
    box-shadow: 0 6px 18px rgba(0,0,0,.25);
    overflow: hidden;
  }
  .card--back { left: 40px; }
  .card--front { left: 620px; }

  /* Back */
  .back-band {
    position: absolute; left: 0; top: 38px; width: 360px; height: 46px;
    background: linear-gradient(90deg, var(--crimson-dark), var(--crimson));
    clip-path: polygon(0 0, 100% 0, 88% 100%, 0 100%);
  }
  .brand {
    display: flex; align-items: center; gap: 8px;
    font-weight: 700; letter-spacing: 1px; text-transform: uppercase;
  }
  .brand__mark { width: 14px; height: 14px; background: var(--red); flex: none; }
  .back-band .brand {
    position: absolute; left: 22px; top: 12px; color: #fff; font-size: 19px;
  }
  .back-logo-spot { position: absolute; right: 30px; top: 22px; }
  .back-logo-spot .brand { color: var(--crimson); font-size: 13px; }
  .back-title {
    position: absolute; left: 30px; top: 108px;
    color: var(--red); font-size: 22px; font-weight: 700;
  }
  .write-lines { position: absolute; left: 30px; right: 30px; top: 150px; }
  .write-lines span {
    display: block; height: 26px; border-bottom: 1px solid var(--rule);
  }
  .back-foot {
    position: absolute; left: 0; right: 0; bottom: 0; height: 12px;
    background: var(--crimson);
  }

  /* Front */
  .front-logo { position: absolute; right: 26px; top: 36px; }
  .front-logo .brand { color: var(--crimson); font-size: 20px; }
  .portrait {
    position: absolute; left: 40px; top: 96px; width: 150px; height: 160px;
    background: linear-gradient(180deg, #7a5238 0%, #4a3228 55%, #1c1c1c 100%);
    border-radius: 4px 4px 0 0;
  }
  .name-plate {
    position: absolute; left: 0; bottom: 12px; width: 330px; height: 66px;
    background: var(--black);
    clip-path: polygon(0 0, 88% 0, 100% 100%, 0 100%);
  }
  .name-plate__accent {
    position: absolute; left: 0; bottom: 12px; width: 350px; height: 70px;
    background: var(--red);
    clip-path: polygon(86% 0, 89% 0, 100% 100%, 97% 100%);
  }
  .name-plate h1 {
    position: absolute; left: 30px; top: 10px;
    color: var(--red); font-size: 24px; font-weight: 700;
  }
  .name-plate p {
    position: absolute; left: 30px; top: 40px;
    color: #fff; font-size: 16px; font-weight: 400;
  }
  .contact {
    position: absolute; left: 290px; top: 150px;
    list-style: none; color: var(--ink); font-size: 14px;
  }
  .contact li { display: flex; align-items: center; gap: 8px; margin-bottom: 7px; }
  .contact svg { width: 14px; height: 14px; fill: var(--crimson); flex: none; }
  .front-foot {
    position: absolute; left: 0; right: 0; bottom: 0; height: 12px;
    background: var(--crimson);
  }
</style>
</head>
<body>

<section class="card card--back" aria-label="Card back">
  <div class="back-band">
    <div class="brand"><span class="brand__mark"></span>Brightline Coverage Co.</div>
  </div>
  <h2 class="back-title">Your Text Here</h2>
  <div class="write-lines"><span></span><span></span><span></span><span></span><span></span></div>
  <div class="back-foot"></div>
</section>

<section class="card card--front" aria-label="Card front">
  <div class="front-logo">
    <div class="brand"><span class="brand__mark"></span>Brightline Coverage Co.</div>
  </div>
  <div class="portrait" role="img" aria-label="Portrait photo of the agent"></div>
  <div class="name-plate__accent"></div>
  <div class="name-plate">
    <h1>Marla Tovesby</h1>
    <p>Insurance Agent</p>
  </div>
  <ul class="contact">
    <li>
      <svg viewBox="0 0 16 16" aria-hidden="true"><path d="M8 1 1 7h2v8h4v-5h2v5h4V7h2z"/></svg>
      NC &amp; SC
    </li>
    <li>
      <svg viewBox="0 0 16 16" aria-hidden="true"><path d="M3 1h3l1.5 4-2 1.2a9 9 0 0 0 4.3 4.3L11 8.5l4 1.5v3a2 2 0 0 1-2 2A12 12 0 0 1 1 3a2 2 0 0 1 2-2z"/></svg>
      704.555.0182
    </li>
    <li>
      <svg viewBox="0 0 16 16" aria-hidden="true"><path d="M1 3h14v10H1zm1.5 1.2v.3L8 8.6l5.5-4.1v-.3z"/></svg>
      marlatovesby@quillmail.example
    </li>
  </ul>
  <div class="front-foot"></div>
</section>

</body>
</html>
```